Business Card Design Project

Hello
I want a Simple Business card that uses the company logo that is easily reasonable but looks professional as I am an IT Services company and would look to share these cards with prospective clients.
The details are:
Kestrel Arc Solutions
14 Morrow Lane
Birmingham
B7 4QX
Telephone 0845 217 6640
I would like my name Oliver Hastings and my title Director on the card.
Target Market(s)
IT Professionals
Industry/Entity Type
Business

```html
<!DOCTYPE html>
<html lang="en">
<head>
<meta charset="UTF-8">
<title>Kestrel Arc Solutions – Business Card</title>
<link rel="stylesheet" href="https://fonts.googleapis.com/css2?family=Lato:wght@400;700&display=swap">
<style>
  :root {
    --backdrop: #5b5b5b;
    --card: #ffffff;
    --ink: #1f1f1f;
    --green-deep: #1b8a3a;
    --green-mid: #3fa535;
    --green-lime: #a9cf38;
    --green-pale: #d6e98a;
    --leaf-yellow: #e4e878;
    --white: #ffffff;
  }
  * { box-sizing: border-box; margin: 0; padding: 0; }
  html, body {
    width: 1200px;
    height: 900px;
    overflow: hidden;
    background: var(--backdrop);
    font-family: "Lato", Arial, sans-serif;
  }
  .card {
    position: absolute;
    left: 75px;
    top: 150px;
    width: 1050px;
    height: 600px;
    background: var(--card);
    overflow: hidden;
  }
  .brand {
    position: absolute;
    left: 60px;
    top: 70px;
    display: flex;
    align-items: center;
    gap: 16px;
  }
  .brand-dot {
    width: 34px;
    height: 34px;
    border-radius: 50%;
    background: var(--green-lime);
  }
  .brand-name {
    font-weight: 700;
    font-size: 40px;
    color: var(--ink);
    letter-spacing: -0.5px;
  }
  .tree-art {
    position: absolute;
    left: 720px;
    top: 40px;
    width: 270px;
    height: 390px;
    border-radius: 135px 135px 24px 24px;
    background: radial-gradient(ellipse at 50% 35%, var(--green-lime) 0%, var(--green-pale) 55%, var(--leaf-yellow) 80%, rgba(228, 232, 120, 0) 100%);
  }
  .person {
    position: absolute;
    left: 60px;
    top: 200px;
  }
  .person-name {
    font-size: 48px;
    font-weight: 400;
    color: var(--ink);
    line-height: 1.1;
  }
  .person-name strong { font-weight: 700; }
  .person-title {
    margin-top: 6px;
    font-size: 27px;
    font-weight: 700;
    letter-spacing: 1.5px;
    color: var(--green-deep);
    text-transform: uppercase;
  }
  .phone {
    position: absolute;
    left: 60px;
    top: 318px;
    font-size: 28px;
    color: var(--ink);
  }
  .phone-label { font-weight: 700; }
  .footer-band {
    position: absolute;
    left: 0;
    right: 0;
    bottom: 0;
    height: 170px;
    background: linear-gradient(to bottom, var(--green-pale) 0%, var(--green-lime) 12%, var(--green-mid) 30%, var(--green-deep) 50%, var(--green-deep) 100%);
  }
  .address {
    position: absolute;
    left: 60px;
    right: 40px;
    bottom: 38px;
    font-size: 28px;
    font-weight: 400;
    letter-spacing: 1.2px;
    color: var(--white);
    text-transform: uppercase;
    white-space: nowrap;
  }
</style>
</head>
<body>
  <main class="card">
    <div class="tree-art" role="img" aria-label="Illustration of a stylised tree with round green and yellow leaf clusters"></div>
    <div class="footer-band" role="img" aria-label="Decorative green wave bands along the bottom edge"></div>

    <div class="brand">
      <span class="brand-dot"></span>
      <span class="brand-name">Kestrel Arc Solutions</span>
    </div>

    <div class="person">
      <h1 class="person-name">Oliver <strong>Hastings</strong></h1>
      <p class="person-title">Director</p>
    </div>

    <p class="phone"><span class="phone-label">PHONE:</span> 0845 217 6640</p>

    <p class="address">Kestrel Arc Solutions, 14 Morrow Lane, Birmingham B7 4QX</p>
  </main>
</body>
</html>
```